Private law enforcement protective services needs a kick ass brochure

We need a brochure that tops the security competition. We are a Pennsylvania based company providing law enforcement officers to the private sector to take the place of regular security officers. We are peacekeepers with the powers of arrest for any major crime committed in our presence. Our customers will get so much more by using our services over regular security. All of our officers attend annual training to stay up to date and sharp in their skills. We would like to see a design that uses the colors Royal blue, black, and grays. The final design should communicate better service over regular security yet have that soft touch and caring feeling. We want to be taken serious yet not scary. We want prospective customers to say WOW... we need to use them rather than regular security guards. We also offer K-9 services. Drug searches as well as explosive searches. THIS NEEDS TO GO ON A TRI FOLD BROCHURE. I already have a website. Www.marlowridgepatrol.com

Target Market(s)

Any business or entity where security or protective services will be needed. We provide services for events like Fairs, carnivals, churches, retail stores, large events, hostile terminations, post disaster sites, overarching of work crews in hostile areas, special celebrations, parades, sporting events,

Industry/Entity Type

Security Service

Font styles to use
Sans Serif

Requirements
Must have
• We need to have a strong professional look yet not too aggressive. DO NOT CALL OUR SERVICES SECURITY !!!! We are PEACEKEEPERS. We Keep the Peace. We provide services all across the state of Pennsylvania. We are one of Pennsylvania's best kept secrets.
Nice to have
• Pictures of Police cars, Officers on patrol at an event,

```html
<!DOCTYPE html>
<html lang="en">
<head>
<meta charset="utf-8">
<title>Marlow Ridge Patrol – Tri-fold Brochure</title>
<link href="https://fonts.googleapis.com/css2?family=Arimo:wght@400;700&family=Montserrat:wght@700;800&family=Open+Sans:wght@400&display=swap" rel="stylesheet">
<style>
  :root{
    --royal:#3a3f9e;
    --royal-deep:#2e3390;
    --ink:#1d1d1f;
    --char:#2b2b2d;
    --graphite:#4a4a4d;
    --paper:#ffffff;
    --stage:#a6a6a6;
    --rule:#111;
    --text:#222;
  }
  *{box-sizing:border-box;margin:0;padding:0}
  html,body{width:1154px;height:1200px;overflow:hidden;background:var(--stage)}
  body{font-family:"Arimo",Arial,sans-serif;color:var(--text);position:relative}

  .spread{position:absolute;left:177px;width:800px;height:566px;background:var(--paper);border:1px solid var(--rule);overflow:hidden}
  .spread--outside{top:22px}
  .spread--inside{top:610px}

  .body-copy{font-size:7.6px;line-height:1.42;text-align:justify;color:var(--text)}
  .photo{position:absolute}
  .band{position:absolute;left:0;width:100%;top:186px;height:193px;background:var(--royal-deep)}

  /* outside */
  .cover-panel{position:absolute;top:0;height:100%}
  .panel-left{left:0;width:266px}
  .panel-mid{left:266px;width:267px}
  .panel-right{left:533px;width:267px}
  .panel-left .copy-top{position:absolute;left:24px;top:30px;width:220px}
  .panel-left .copy-bottom{position:absolute;left:24px;top:423px;width:220px}
  .patch{position:absolute;left:34px;top:165px;width:194px;height:225px}
  .photo-mid-top{left:0;top:0;width:100%;height:186px;background:radial-gradient(ellipse at 55% 45%,#5a5a5c 0%,#2e2e30 60%,#1a1a1b 100%)}
  .photo-mid-bottom{left:0;top:379px;width:100%;height:187px;background:radial-gradient(ellipse at 45% 50%,#5c5b57 0%,#2f2f30 60%,#1b1b1c 100%)}
  .photo-right{left:0;top:0;width:100%;height:100%;background:linear-gradient(160deg,#4c4c4e 0%,#2a2a2c 45%,#1c1c1d 75%,#2b2b2d 100%)}
  .contact{position:absolute;left:0;top:186px;width:100%;height:193px;display:flex;flex-direction:column;align-items:center;justify-content:center;font-family:"Open Sans",Arial,sans-serif;color:#fff;font-size:15.5px;line-height:1.3;text-align:center}
  .contact-icons{display:flex;gap:7px;margin-bottom:16px}
  .brand{position:absolute;display:flex;flex-direction:column;align-items:center;gap:8px;font-family:"Montserrat",Arial,sans-serif;font-weight:800;color:#fff;text-align:center;line-height:1.05;letter-spacing:.5px}
  .panel-right .brand{left:20px;width:227px;top:230px;font-size:26px}
  .brand-mark{width:38px;height:38px;border-radius:50%;border:3px solid #fff}

  /* inside */
  .photo-lights{left:266px;top:256px;width:270px;height:310px;background:radial-gradient(circle at 20% 35%,#c02a4a 0%,#6d1a3c 28%,transparent 55%),radial-gradient(circle at 70% 70%,#3f55c8 0%,#1a2360 35%,transparent 60%),linear-gradient(180deg,#3a1430 0%,#0d0f22 100%)}
  .photo-dark{left:0;top:415px;width:266px;height:151px;background:linear-gradient(180deg,#13162a 0%,#0a0b16 100%)}
  .who{position:absolute;left:0;top:0;width:266px;height:415px;background:var(--paper);padding:18px 14px 0 16px}
  .heading{font-family:"Montserrat",Arial,sans-serif;font-weight:700;font-size:8.6px;line-height:1.2;color:var(--ink);text-transform:uppercase}
  .who .heading{margin-left:10px;margin-bottom:4px}
  .who p{margin-bottom:8px}
  .typical{position:absolute;left:290px;top:18px;width:222px}
  .typical .heading{margin-bottom:9px}
  .inside-right{position:absolute;left:536px;top:0;width:264px;height:566px}
  .inside-right .brand{left:22px;width:220px;top:40px;font-size:27px;color:var(--royal)}
  .inside-right .brand-mark{border-color:var(--royal)}
  .inside-right .heading{position:absolute;left:20px;top:330px;width:220px}
  .services{position:absolute;left:18px;top:380px;width:236px;display:grid;grid-template-columns:1fr 1fr;row-gap:14px;column-gap:6px;list-style:none}
  .services li{display:flex;align-items:center;gap:8px;font-size:8px;line-height:1.25;color:var(--text);height:44px}
  .service-dot{flex:none;width:40px;height:40px;border-radius:50%;border:2px solid var(--royal);background:radial-gradient(circle,#8c8c8e 0 9px,#fff 10px)}
</style>
</head>
<body>

<!-- Outside spread -->
<section class="spread spread--outside" aria-label="Brochure outside">
  <div class="band"></div>

  <div class="cover-panel panel-left">
    <p class="body-copy copy-top">The Pennsylvania State Constable is one of the most overlooked entities. Many organizations utilize regular security officers for services to oversee their events, locations, and products simply because they are not aware that constables exist. A Pennsylvania State Constable can perform many of these tasks and address the majority of one’s concerns and needs the same as a security officer can. A Pennsylvania State Constable is a Peace Keeper. We keep the peace wherever that may be, for whatever event or incident may be occurring. Unlike security guards,</p>
    <svg class="patch" viewBox="0 0 194 225" role="img" aria-label="Embroidered constable shoulder patch">
      <path d="M8 30 Q97 -6 186 30 L170 200 Q97 232 24 200 Z" fill="#1e1e20" stroke="#777" stroke-width="5"/>
    </svg>
    <p class="body-copy copy-bottom">Pennsylvania State Constables are required to attend basic training as well as annual updates to stay refreshed. Security guards do not have any of those requirements. If you have an event, location, or incident that is of concern for the safety and protection of all involved, contact us today to see how we may help you. Not only will you be getting that presence and deterrent, but you will also be getting an actual law enforcement officer. Get more for your money!</p>
  </div>

  <div class="cover-panel panel-mid">
    <div class="photo photo-mid-top" role="img" aria-label="Photo of a constable patch on a dark table"></div>
    <div class="contact">
      <div class="contact-icons">
        <svg width="22" height="22" viewBox="0 0 22 22" aria-hidden="true"><circle cx="11" cy="11" r="10" fill="none" stroke="#fff" stroke-width="1.4"/><path d="M8 5.5c-1.5 1-1.6 3.2 0 6.3s3.8 4.8 5.5 4.7l1.2-1.8-2-1.4-1 .8c-.9-.5-2-2-2.4-3l.9-.8-1-2.3Z" fill="#fff"/></svg>
        <svg width="22" height="22" viewBox="0 0 22 22" aria-hidden="true"><circle cx="11" cy="11" r="10" fill="none" stroke="#fff" stroke-width="1.4"/><rect x="5.5" y="7" width="11" height="8" fill="#fff"/><path d="M5.5 7 11 11.5 16.5 7" fill="none" stroke="var(--royal-deep)" stroke-width="1"/></svg>
        <svg width="22" height="22" viewBox="0 0 22 22" aria-hidden="true"><circle cx="11" cy="11" r="10" fill="none" stroke="#fff" stroke-width="1.4"/><circle cx="11" cy="11" r="6" fill="none" stroke="#fff" stroke-width="1.1"/><ellipse cx="11" cy="11" rx="2.6" ry="6" fill="none" stroke="#fff" stroke-width="1"/><path d="M5 11h12M6 8h10M6 14h10" stroke="#fff" stroke-width=".9"/></svg>
      </div>
      <span>+0 123 456 789</span>
      <span>info@yourmail.com</span>
      <span>www.yourcompany.com</span>
    </div>
    <div class="photo photo-mid-bottom" role="img" aria-label="Photo of a gold badge on a dark table"></div>
  </div>

  <div class="cover-panel panel-right">
    <div class="photo photo-right" role="img" aria-label="Photo of a handgun, holster, patch, badge and handcuffs on a dark table"></div>
    <div class="brand"><span class="brand-mark"></span>MARLOW RIDGE PATROL</div>
  </div>
</section>

<!-- Inside spread -->
<section class="spread spread--inside" aria-label="Brochure inside">
  <div class="photo photo-dark" role="img" aria-label="Dark background of police car lights"></div>
  <div class="photo photo-lights" role="img" aria-label="Photo of a uniformed officer in front of police car lights at night"></div>

  <div class="who">
    <h2 class="heading">Who We Are</h2>
    <div class="body-copy">
      <p>Under Pennsylvania Law, Constables are Public Officers elected or appointed to their position in accordance with the laws of elections.</p>
      <p>A Constable is a sworn Law Enforcement/Peace Officer that can arrest for felony crimes and breaches of peace committed in his presence, or by warrant anywhere in the Commonwealth.</p>
      <p>A Constable is also an officer empowered to carry out the business of the statewide district court system by serving warrants of arrest, mental health warrants, transporting prisoners, service of summons, complaints and subpoenas, and enforcing protection from abuse orders, as well as orders of eviction and judgement levies.</p>
      <p>Constables are also charged with maintaining order at the election polls and ensuring that no qualified elector is obstructed from voting. Constables are the only law enforcement officials permitted at the polls on election day.</p>
      <p>While Constables primarily serve the Courts, they belong to the executive branch of government.</p>
      <p>Constables are empowered to enforce both criminal and civil laws. Police officers are empowered to enforce criminal and traffic laws. The sheriff is empowered to enforce criminal, civil, and traffic laws. The District Attorney is the chief law enforcement officer of the County.</p>
    </div>
  </div>

  <div class="typical">
    <h2 class="heading">Typical events/locations at which Pennsylvania State Constables provide services:</h2>
    <p class="body-copy">Pennsylvania State Constables are Peace Keepers. A Constable may make a warrant less arrest for any breach of the peace in his or her presence. A breach of the peace by definition in Pennsylvania is any offence that is considered a misdemeanor or felony. Constables work side by side with local and state authorities in many cases around the state. The Pennsylvania State Constable is one of the most overlooked entities around Pennsylvania today. Constables are not security guards, however any where you find event security, you would very easily be able to replace them with a Constable. We are able to function at events and incidents much like a security guard. Our Pennsylvania State Constables will maintain the peace, give you that added presence of law enforcement and peace of mind you deserve.</p>
  </div>

  <div class="inside-right">
    <div class="brand"><span class="brand-mark"></span>MARLOW RIDGE PATROL</div>
    <h2 class="heading">Typical events/locations at which Pennsylvania State Constables provide services:</h2>
    <ul class="services">
      <li><span class="service-dot"></span>Public<br>Events</li>
      <li><span class="service-dot"></span>Construction /<br>Utility Job Sites</li>
      <li><span class="service-dot"></span>Crowd<br>Control</li>
      <li><span class="service-dot"></span>Emergencies/<br>Disasters</li>
      <li><span class="service-dot"></span>Retail</li>
      <li><span class="service-dot"></span>Place of<br>Employment</li>
    </ul>
  </div>
</section>

</body>
</html>
```